Website Design for Qolva-iX Software Solutions

Our company (IT) develops (3 main markets):
- Software for selfservice kiosks
- Web- and Mobile applications
- Embedded Software

```html
<!DOCTYPE html>
<html lang="nl">
<head>
<meta charset="utf-8">
<title>Qolva-iX Software Solutions</title>
<link rel="stylesheet" href="https://fonts.googleapis.com/css2?family=Arimo:wght@400;700&family=Open+Sans:wght@300;400&family=Roboto+Condensed:wght@400;700&display=swap">
<style>
:root{
  --green-bg:#7cb82a;
  --green-dark:#5f9a16;
  --page:#f1f2f3;
  --blue:#1d6fa8;
  --blue-dark:#0d4f85;
  --blue-light:#3aa0e0;
  --heading-blue:#1a5f97;
  --orange:#f08a12;
  --orange-light:#fbb04a;
  --text:#555;
  --text-dark:#2c2c2c;
  --footer:#555758;
  --accent-green:#3e8f1a;
}
*{box-sizing:border-box;margin:0;padding:0}
html,body{width:1200px;height:784px;overflow:hidden}
body{
  position:relative;
  background:radial-gradient(ellipse at 50% 40%,#a4d63e 0%,var(--green-bg) 55%,var(--green-dark) 100%);
  font-family:"Arimo",Arial,sans-serif;color:var(--text);
}
.page{position:absolute;left:139px;top:0;width:924px;height:784px;background:var(--page);box-shadow:0 0 12px rgba(0,0,0,.35)}
.abs{position:absolute}
.header{left:0;top:0;width:924px;height:88px;background:linear-gradient(#fff,#e6e8ea)}
.brand{left:20px;top:16px;font-family:"Roboto Condensed",sans-serif;font-weight:700;font-size:44px;letter-spacing:2px;color:var(--orange)}
.nav{top:27px;height:25px;width:91px;border-radius:6px;background:linear-gradient(var(--orange-light),var(--orange));color:#fff;font-size:12px;text-align:center;line-height:25px;box-shadow:0 1px 2px rgba(0,0,0,.3)}
.hero{left:0;top:88px;width:924px;height:213px;background:linear-gradient(90deg,var(--blue-dark) 0%,var(--blue) 45%,#3d8cc4 100%)}
.welcome{left:28px;top:45px;color:#fff;font-size:18px}
.welcome b{font-style:italic;font-weight:400;font-size:26px}
.hero-text{left:28px;top:84px;width:335px;color:#fff;font-size:10.5px;line-height:12.5px}
.hero-text .lead{color:var(--blue-light);font-weight:700}
.hero-text p+p{margin-top:12px}
.hero-visual{left:361px;top:20px;width:240px;height:281px;background:linear-gradient(180deg,rgba(110,180,225,.55) 0%,rgba(40,120,180,.6) 55%,rgba(20,80,130,.35) 100%)}
.slogan{left:601px;top:129px;width:323px;height:128px;background:linear-gradient(#fff,#dfe2e5)}
.slogan .s1{position:absolute;left:30px;top:12px;font-family:"Open Sans",sans-serif;font-size:29px;color:var(--accent-green)}
.slogan .s2{position:absolute;left:30px;top:44px;font-family:"Open Sans",sans-serif;font-size:41px;color:var(--text-dark);letter-spacing:.5px}
.slogan .s3{position:absolute;left:32px;top:99px;font-size:11.5px;color:var(--text-dark)}
.service{top:308px;height:96px}
.service.light{background:linear-gradient(#fff,#e9eaeb)}
.service.grey{background:linear-gradient(#dcdee0,#c8cbce)}
.service .icon{position:absolute;left:14px;top:10px;width:80px;height:76px;border-radius:10px}
.service .t1{position:absolute;left:110px;top:15px;font-size:18px;color:#444}
.service .t2{position:absolute;left:110px;top:36px;font-family:"Roboto Condensed",sans-serif;font-weight:700;font-size:29px;color:var(--heading-blue)}
.service .more{position:absolute;right:12px;top:74px;width:82px;height:16px;border-radius:8px;background:#cfd1d3;font-size:10.5px;color:#444;text-align:center;line-height:16px}
.kiosk-photo{left:25px;top:421px;width:103px;height:142px;border:1px solid #ccc;background:linear-gradient(#fff,#e3e5e8)}
.kiosk-photo div{position:absolute;left:28px;top:10px;width:46px;height:122px;border-radius:4px;background:linear-gradient(90deg,#8c9299,#d3d7db,#7d848b)}
.sec-title{font-size:19px;color:var(--heading-blue)}
.body-text{font-size:10.5px;line-height:13px;color:#777;text-align:justify}
.contact{left:25px;top:577px;width:492px;height:110px;background:#e2e4e6}
.contact .bar{position:absolute;left:8px;top:10px;width:474px;height:26px;background:linear-gradient(90deg,var(--blue-dark),var(--blue))}
.contact .bar span{position:absolute;left:34px;top:2px;color:#fff;font-size:19px}
.contact .bar i{position:absolute;left:6px;top:3px;width:20px;height:20px;border-radius:50%;background:radial-gradient(circle at 40% 35%,#bfe3f7,#3a8fc8);border:2px solid #fff}
.contact .info{position:absolute;font-size:10.5px;line-height:13px;color:#555}
.contact .follow{position:absolute;left:368px;top:44px;font-size:15px;color:#444}
.contact .social{position:absolute;top:66px;width:30px;height:30px;border-radius:4px}
.cert-list{left:545px;top:452px;width:360px;height:228px}
.cert{position:absolute;left:0;width:360px;background:linear-gradient(#e6e7e8,#d5d7d9)}
.cert .badge{position:absolute;left:6px;top:5px;width:67px;height:64px;border:2px solid #fff;box-shadow:0 0 2px rgba(0,0,0,.4)}
.cert h4{position:absolute;left:83px;top:4px;font-size:12px;color:#222}
.cert p{position:absolute;left:83px;top:20px;width:268px;font-size:10px;line-height:13px;color:#888}
.footer{left:0;top:713px;width:924px;height:71px;background:linear-gradient(#6c6e70,var(--footer))}
.footer .link{position:absolute;top:32px;font-size:11.5px;color:#ddd}
.footer .sep{position:absolute;top:28px;width:1px;height:19px;background:#888}
.footer .copy{position:absolute;left:712px;top:30px;font-size:11.5px;color:#ddd}
</style>
</head>
<body>
<div class="page">
  <header class="abs header">
    <div class="abs brand">QOLVA-IX</div>
    <div class="abs nav" style="left:594px">Nieuws</div>
    <div class="abs nav" style="left:702px">Wat wij Doen</div>
    <div class="abs nav" style="left:814px">Contact us</div>
  </header>

  <section class="abs hero">
    <div class="abs welcome">Welcome to <b>QOLVA-IX</b></div>
    <div class="abs hero-text">
      <p><span class="lead">Some text will come here will be replaced by the original text</span><br>Some text will come here will be replaced by the original text Some text will come here will be replaced by the original text some text<br>Some text will come here will be replaced</p>
      <p>Some text will come here will be replaced by the original<br>text Some text will come here will be replaced by the original text<br>some text Some text will come here will be replaced</p>
    </div>
  </section>
  <div class="abs hero-visual" role="img" aria-label="Globe with a team of business people standing in front"></div>
  <div class="abs slogan">
    <span class="s1">Doordacht</span>
    <span class="s2">EN EFFICIENT</span>
    <span class="s3">en nooit bang om buiten de standaarden te denken!</span>
  </div>

  <div class="abs service light" style="left:0;width:309px">
    <div class="icon" role="img" aria-label="Gear and kiosk screen icon" style="background:linear-gradient(#e4e5e6,#a9acb0)"></div>
    <span class="t1">Software for selfservice</span>
    <span class="t2">KIOSKS</span>
    <span class="more">Read more &gt;&gt;</span>
  </div>
  <div class="abs service grey" style="left:310px;width:302px">
    <div class="icon" role="img" aria-label="Globe button icon" style="background:linear-gradient(#eef0f1,#9a9ea3)"></div>
    <span class="t1">Web and Mobile</span>
    <span class="t2">APPLICATIONS</span>
    <span class="more">Read more &gt;&gt;</span>
  </div>
  <div class="abs service grey" style="left:613px;width:302px">
    <div class="icon" role="img" aria-label="Software box with disc icon" style="background:linear-gradient(#6d7074,#3d4043)"></div>
    <span class="t1" style="left:120px">Embedded</span>
    <span class="t2">SOFTWARES</span>
    <span class="more">Read more &gt;&gt;</span>
  </div>

  <div class="abs kiosk-photo" role="img" aria-label="Self-service kiosk terminal"><div></div></div>
  <h2 class="abs sec-title" style="left:141px;top:419px">Kiosks</h2>
  <div class="abs body-text" style="left:141px;top:444px;width:376px">
    <p>Some text will come here will be replaced by the real and the attractive original text Some text Some text will come here will be replaced by the real and the attractive original Some text will come here will be replaced by the real and the attractive original text Some text Some text will come here will be replaced by the real and the attractive original</p>
    <p style="margin-top:13px">Some text will come here will be replaced by the real and the attractive original text Some text Some text will come here will be replaced Some text Some text will come here will be replaced</p>
  </div>

  <div class="abs contact">
    <div class="bar"><i></i><span>Contact us</span></div>
    <div class="info" style="left:17px;top:44px">Qolva-iX Software Solutions<br>Veldmolenkade 42<br>3012 ZX Havenstad<br>Telefoon: +31(0)10 555 01 23</div>
    <div class="info" style="left:179px;top:70px">E-mail:&nbsp; info@qolva-ix.nl<br>Website: www.qolva-ix.nl</div>
    <div class="follow">Follow us on:</div>
    <div class="social" style="left:372px;background:#3b5a9a"></div>
    <div class="social" style="left:406px;background:#4fb6e8"></div>
  </div>

  <h2 class="abs sec-title" style="left:543px;top:421px">Our Certified</h2>
  <div class="abs cert-list">
    <div class="cert" style="top:0;height:74px">
      <div class="badge" style="background:#e8832a"></div>
      <h4>Some text will come here</h4>
      <p>Some text will come here will be replaced by the real and the attractive original text Some text Some text will come here will be replaced by the real and the attractive original</p>
    </div>
    <div class="cert" style="top:76px;height:74px">
      <div class="badge" style="background:#c8252a"></div>
      <h4>Some text will come here</h4>
      <p>Some text will come here will be replaced by the real and the attractive original text Some text Some text will come here will be replaced by the real and the attractive original</p>
    </div>
    <div class="cert" style="top:152px;height:76px">
      <div class="badge" style="background:#2a2a2a"></div>
      <h4>Some text will come here</h4>
      <p>Some text will come here will be replaced by the real and the attractive original text Some text Some text will come here will be replaced by the real and the attractive original</p>
    </div>
  </div>

  <footer class="abs footer">
    <span class="link" style="left:40px">Nieuws</span>
    <span class="sep" style="left:91px"></span>
    <span class="link" style="left:120px">Wat wij Doen</span>
    <span class="sep" style="left:210px"></span>
    <span class="link" style="left:228px">Contact us</span>
    <span class="copy">Copyright © 2011 Qolva-ix.com</span>
  </footer>
</div>
</body>
</html>
```